5x5 Pop Up Display, Company Logo With Text and Graphics for Tradeshow Display

Design for a 5ft x 5ft pop up trade show display that will sit on top of a table. I usually prefer clean, somewhat minimalist designs. We are a food service company but it's not a requirement to have photos of food. Design elements should compliment the table cloth that we have for the booth. The below may be included depending on the design aesthetic.
Service Provided: Daily Meal Service, Kitchen Management
"Nationwide Footprint"
"Grassroots Service"
"Fresh Scratch Cooking"
"Custom Menus"
"Made To Order Meals"

```html
<!DOCTYPE html>
<html lang="en">
<head>
<meta charset="utf-8">
<title>Hale Hearth – Daily Meal Service Display</title>
<link href="https://fonts.googleapis.com/css2?family=Poppins:wght@600;700;800&family=Jost:wght@500&display=swap" rel="stylesheet">
<style>
  :root {
    --ink: #231f20;
    --orange: #e2673a;
    --green: #7c9f5a;
    --green-dark: #2f6b1f;
    --green-pale: #b7cfa0;
    --paper: #ffffff;
    --scene-top: #e4e7e3;
    --scene-mid: #bfc3c0;
    --scene-low: #3f7a34;
  }
  * { margin: 0; padding: 0; box-sizing: border-box; }
  html, body { width: 1200px; height: 1200px; overflow: hidden; background: var(--paper); }
  .display {
    position: relative;
    width: 1200px;
    height: 1200px;
    background: var(--paper);
    font-family: 'Poppins', sans-serif;
    color: var(--ink);
    overflow: hidden;
  }
  .swoosh { position: absolute; left: 0; top: 0; width: 1200px; height: 320px; }
  .brand {
    position: absolute;
    left: 0; right: 0; top: 70px;
    display: flex; justify-content: center; align-items: center; gap: 18px;
  }
  .brand-name {
    font-family: 'Poppins', sans-serif;
    font-weight: 800;
    font-size: 64px;
    line-height: 0.95;
    text-align: center;
    text-transform: uppercase;
    color: var(--ink);
    letter-spacing: 1px;
  }
  .brand-mark {
    width: 44px; height: 44px; border-radius: 50%;
    background: var(--green);
    align-self: flex-start; margin-top: 4px;
  }
  .headline {
    position: absolute; left: 0; right: 0; top: 335px;
    text-align: center;
    font-weight: 800;
    font-size: 134px;
    line-height: 1;
    letter-spacing: -1px;
  }
  .headline .accent { color: var(--orange); display: block; font-size: 128px; margin-top: 6px; }
  .side-disc {
    position: absolute; left: 12px; top: 590px;
    width: 150px; height: 150px; border-radius: 50%;
    background: radial-gradient(circle at 50% 60%, #f6d27a 0%, #e98a45 45%, #8fb84a 100%);
  }
  .services {
    position: absolute; left: 120px; top: 670px;
    width: 1000px; height: 150px;
  }
  .services-frame {
    position: absolute; inset: 34px 0 0 0;
    border: 5px solid var(--green);
    border-radius: 18px;
  }
  .services-title {
    position: absolute; left: 50%; top: 0; transform: translateX(-50%);
    background: var(--paper); padding: 0 26px;
    font-family: 'Jost', sans-serif; font-weight: 500;
    font-size: 50px; line-height: 64px; color: var(--green);
    white-space: nowrap;
  }
  .services-list {
    position: absolute; left: 0; right: 0; top: 72px;
    text-align: center;
    font-weight: 600; font-size: 27px; line-height: 36px;
  }
  .scene {
    position: absolute; left: 0; right: 0; top: 840px; bottom: 0;
    background: linear-gradient(180deg, var(--paper) 0%, var(--scene-top) 35%, var(--scene-mid) 70%, var(--scene-low) 100%);
  }
</style>
</head>
<body>
<main class="display">
  <svg class="swoosh" viewBox="0 0 1200 320" aria-hidden="true">
    <path d="M20 20 C120 170 320 300 600 320 C880 300 1080 170 1200 0 L1200 40 C1070 200 860 320 600 330 C330 320 140 190 20 20 Z" fill="var(--green-pale)"/>
    <path d="M20 20 L95 20 C150 140 230 230 250 250 C150 190 70 110 20 20 Z" fill="var(--green)"/>
    <path d="M1080 0 L1200 0 L1200 30 C1100 190 950 290 780 320 C930 260 1040 140 1080 0 Z" fill="var(--green)"/>
    <path d="M1150 0 L1200 0 L1200 30 C1185 20 1165 10 1150 0 Z" fill="var(--green-dark)"/>
  </svg>

  <header class="brand">
    <div class="brand-name">Hale<br>Hearth</div>
    <span class="brand-mark" aria-hidden="true"></span>
  </header>

  <h1 class="headline">DAILY MEAL<span class="accent">SERVICE</span></h1>

  <div class="side-disc" aria-hidden="true"></div>

  <section class="services">
    <div class="services-frame"></div>
    <h2 class="services-title">Kitchen Management</h2>
    <p class="services-list">Nationwide Footprint • Grassroots Service • Fresh Scratch<br>Cooking • Custom Menus • Made To Order Meals</p>
  </section>

  <div class="scene" role="img" aria-label="Illustration of two staff members holding plates of food in front of a columned house, with green hedges and a dotted pattern"></div>
</main>
</body>
</html>
```